Powerpoint design for Halvora Trade Allies

We would like to have a Power point template/design with flexibilities and good opportunities to do changes.
• Be able to change in image background
• Themes are HTA colors and complementary colors. Please come with suggestions.
• Alternate white and blue background
• Standard functions and opportunities within Powerpoint should be able to be used or be accessible.
• Feel free to change/alter the logo for example remove or separate the text in the logo ("Halvora Trade Allies" ) and the tagline ("we create competitiveness")
• www.halvoratradeallies.se

```html
<!DOCTYPE html>
<html lang="en">
<head>
<meta charset="utf-8">
<title>Halvora Trade Allies — Presentation Template</title>
<link href="https://fonts.googleapis.com/css2?family=Roboto:wght@300;400;500;700&display=swap" rel="stylesheet">
<style>
:root{
  --navy:#0b4a8e;
  --navy-deep:#083d78;
  --mid:#2e62a3;
  --bright:#2196f3;
  --slate:#3d5677;
  --gray:#8c8c8c;
  --gray-light:#a3a3a3;
  --gray-dark:#4b5058;
  --charcoal:#3a4450;
  --paper:#f6f8fb;
  --panel:#e8ebef;
  --white:#ffffff;
}
*{box-sizing:border-box;margin:0;padding:0}
html,body{width:926px;height:1200px;overflow:hidden}
body{font-family:Roboto,Arial,sans-serif;background:linear-gradient(205deg,#8e8e8e 0%,#d6d6d6 17%,#ffffff 36%);position:relative}

/* masthead */
.masthead{position:absolute;left:0;top:0;width:880px;height:130px;text-align:center;color:var(--navy)}
.masthead__mark{position:absolute;left:0;right:0;top:16px;font-size:54px;font-weight:700;letter-spacing:2px;line-height:1}
.masthead__name{position:absolute;left:0;right:0;top:78px;font-size:22px;font-weight:400;line-height:1}
.masthead__tagline{position:absolute;left:0;right:0;top:102px;font-size:11px;letter-spacing:3.2px;line-height:1}

/* deck grid */
.deck{position:absolute;left:22px;top:150px;display:grid;grid-template-columns:repeat(4,198px);grid-template-rows:repeat(7,111px);column-gap:30px;row-gap:39.2px}
.slide{position:relative;overflow:hidden;background:var(--bg);color:var(--ink);box-shadow:0 3px 9px rgba(0,0,0,.28)}
.slide--dark{--bg:var(--navy);--ink:#fff;--soft:rgba(255,255,255,.72);--accent-band:var(--mid)}
.slide--light{--bg:var(--paper);--ink:var(--navy);--soft:#6c7682;--accent-band:var(--navy)}
.slide > *{position:absolute}

.brand{top:5px;right:9px;font-size:7px;font-weight:700;letter-spacing:.3px;color:var(--ink);line-height:1}
.foot{left:11px;right:11px;bottom:3px;display:flex;justify-content:space-between;font-size:2.2px;color:var(--soft);line-height:1}
.title{font-size:4.6px;font-weight:500;line-height:1.2;color:var(--ink)}
.title--center{left:0;right:0;text-align:center}
.sub{font-size:2.2px;color:var(--soft);line-height:1.2}
.copy{font-size:2.1px;line-height:1.45;color:var(--soft)}
.label{font-size:2.5px;font-weight:500;color:var(--ink);line-height:1.3}
.list{font-size:2.6px;line-height:1.45;color:var(--soft);list-style:none}
.list li::before{content:"•";margin-right:2px}

.ph{display:block}
.ph--screen{background:linear-gradient(120deg,#1b2736 0%,#25557c 50%,#6fb8e0 100%)}
.ph--circuit{background:radial-gradient(circle at 45% 55%,#8d949c 0%,#40464e 45%,#1f2328 100%)}
.ph--store{background:linear-gradient(100deg,#b7ada3 0%,#e1d8cf 50%,#9e958c 100%)}
.ph--person-dark{background:linear-gradient(160deg,#1c1c1c 0%,#4d4d4d 60%,#777 100%)}
.ph--mixer{background:linear-gradient(150deg,#2f2a40 0%,#6b5f8a 50%,#a99ac4 100%)}
.ph--tablet{background:linear-gradient(150deg,#eef0f3 0%,#a9b0ba 60%,#6d7580 100%)}
.ph--globe{background:linear-gradient(135deg,#e5eef6 0%,#a8c3da 55%,#5e7b97 100%)}
.ph--chart{background:linear-gradient(135deg,#d9effd 0%,#7cc2f5 45%,#1f86dc 100%)}
.ph--network{background:linear-gradient(90deg,#25292f 0%,#5a6068 45%,#b9b1a7 100%)}
.ph--hand{background:radial-gradient(circle at 50% 45%,#c89a5c 0%,#5a4630 35%,#15161a 80%)}

.dot{border-radius:50%;display:grid;place-items:center;color:#fff}
.dot svg{width:52%;height:52%}
.dot--white{background:#fff;color:var(--navy)}
.dot--gray{background:var(--gray);border:.6px solid rgba(255,255,255,.7)}
.dot--bright{background:var(--bright);border:.6px solid rgba(255,255,255,.7)}
.dot--dark{background:var(--gray-dark)}
.dot--navy{background:var(--navy)}
.glyph{width:5px;height:5px;color:var(--ink)}

.band{left:0;right:0}
.band--accent{background:var(--accent-band)}
.band--gray{background:var(--gray)}
.slide--light .band--gray{background:var(--gray-light)}

.num{font-size:5.6px;font-weight:700;color:var(--ink);margin-right:1.5px}
.tile{display:flex;flex-direction:column;align-items:center;padding:3px 3px 0;text-align:center;color:#fff}
.tile .label{color:#fff;font-size:2.3px;margin-top:3px}
.tile .copy{color:rgba(255,255,255,.82);font-size:1.9px}
.tile svg{width:4.5px;height:4.5px}
.tile--gray{background:var(--gray)}
.tile--mid{background:var(--mid)}
.tile--slate{background:var(--slate)}
.tile--bright{background:var(--bright)}
.tile--navy{background:var(--navy)}

.callout{padding:3px 4px;font-size:2.3px;line-height:1.5;color:rgba(255,255,255,.9)}

.price{display:flex;flex-direction:column;align-items:center;padding-top:7px;text-align:center}
.price__amount{font-size:11px;font-weight:300;line-height:1}
.price__amount small{font-size:3px}
.price__plan{font-size:2.6px;font-weight:700;margin-top:5px}
.price .copy{margin-top:2px;padding:0 3px;font-size:1.9px;color:inherit;opacity:.8}
.price__btn{margin-top:3px;font-size:1.8px;border:.4px solid currentColor;border-radius:2px;padding:.5px 4px;opacity:.8}
.price--white{background:#fff;color:var(--navy)}
.price--gray{background:var(--gray);color:#2c3440}
.price--mid{background:var(--mid);color:#fff}
.price--bright{background:var(--bright);color:#fff}
.price--navy{background:var(--navy-deep);color:#fff}
.price--dark{background:var(--gray-dark);color:#fff}

.legend{font-size:1.8px;color:rgba(255,255,255,.85);line-height:2.1}
.legend i{display:inline-block;width:1.6px;height:1.6px;border-radius:50%;margin-right:1.5px;vertical-align:middle}

.client{font-size:10px;font-weight:700;letter-spacing:.5px;line-height:1}
.caps{font-size:1.9px;font-weight:700;letter-spacing:.2px;color:var(--ink)}
</style>
</head>
<body>

<svg width="0" height="0" style="position:absolute" aria-hidden="true">
  <defs>
    <symbol id="i-clock" viewBox="0 0 24 24"><circle cx="12" cy="12" r="9" fill="currentColor"/><path d="M12 7v5l3 2" stroke="#fff" stroke-width="2.2" fill="none" stroke-linecap="round"/></symbol>
    <symbol id="i-hourglass" viewBox="0 0 24 24"><path d="M7 3h10M7 21h10M8 3l4 9-4 9M16 3l-4 9 4 9" stroke="currentColor" stroke-width="2.2" fill="none" stroke-linecap="round"/></symbol>
    <symbol id="i-target" viewBox="0 0 24 24"><g stroke="currentColor" stroke-width="2.2" fill="none"><circle cx="12" cy="12" r="9"/><circle cx="12" cy="12" r="4.5"/></g><circle cx="12" cy="12" r="1.5" fill="currentColor"/></symbol>
    <symbol id="i-people" viewBox="0 0 24 24"><g fill="currentColor"><circle cx="12" cy="7" r="3.5"/><circle cx="7" cy="15" r="3.5"/><circle cx="17" cy="15" r="3.5"/></g></symbol>
    <symbol id="i-gauge" viewBox="0 0 24 24"><path d="M4 17a8 8 0 0 1 16 0M12 17l4-5" stroke="currentColor" stroke-width="2.2" fill="none" stroke-linecap="round"/></symbol>
    <symbol id="i-globe" viewBox="0 0 24 24"><g stroke="currentColor" stroke-width="2" fill="none"><circle cx="12" cy="12" r="9"/><ellipse cx="12" cy="12" rx="4" ry="9"/><path d="M3 12h18"/></g></symbol>
    <symbol id="i-monitor" viewBox="0 0 24 24"><g stroke="currentColor" stroke-width="2" fill="none"><rect x="3" y="4" width="18" height="12" rx="1"/><path d="M9 20h6M12 16v4"/></g></symbol>
    <symbol id="i-send" viewBox="0 0 24 24"><path d="M3 11l18-8-8 18-2-8z" stroke="currentColor" stroke-width="2" fill="none" stroke-linejoin="round"/></symbol>
    <symbol id="i-search" viewBox="0 0 24 24"><g stroke="currentColor" stroke-width="2.2" fill="none"><circle cx="10" cy="10" r="6"/><path d="M15 15l6 6"/></g></symbol>
    <symbol id="i-bank" viewBox="0 0 24 24"><path d="M3 9l9-5 9 5M5 10v8M10 10v8M14 10v8M19 10v8M3 20h18" stroke="currentColor" stroke-width="2" fill="none"/></symbol>
    <symbol id="i-calendar" viewBox="0 0 24 24"><g stroke="currentColor" stroke-width="2" fill="none"><rect x="4" y="5" width="16" height="15" rx="1"/><path d="M4 10h16M8 3v4M16 3v4"/></g></symbol>
    <symbol id="i-image" viewBox="0 0 24 24"><g stroke="currentColor" stroke-width="2" fill="none"><rect x="3" y="4" width="18" height="16" rx="1"/><path d="M3 17l6-6 5 5 3-3 4 4"/></g></symbol>
    <symbol id="i-pie" viewBox="0 0 24 24"><path d="M12 3a9 9 0 1 0 9 9h-9z" fill="currentColor"/><path d="M14 1.5a8.5 8.5 0 0 1 8.5 8.5H14z" fill="currentColor"/></symbol>
  </defs>
</svg>

<header class="masthead">
  <div class="masthead__mark">HTA</div>
  <div class="masthead__name">Halvora Trade Allies</div>
  <div class="masthead__tagline">We create competitiveness</div>
</header>

<main class="deck">

<!-- row 1 -->
<section class="slide slide--dark">
  <div class="ph ph--screen" style="left:0;top:16px;width:99px;height:40px" role="img" aria-label="Photo: woman touching a holographic data screen"></div>
  <div style="left:104px;top:28px;font-size:9px;font-weight:700;line-height:1">HTA</div>
  <div class="title" style="left:137px;top:27px;width:56px;font-weight:300">Our passion is the key factor for customer success</div>
  <div class="ph ph--circuit" style="left:99px;top:56px;width:50px;height:40px" role="img" aria-label="Photo: retail technology icons over a dark background"></div>
  <div class="ph ph--store" style="left:149px;top:56px;width:49px;height:40px" role="img" aria-label="Photo: shoppers in a bright store"></div>
  <div class="dot dot--white" style="left:13px;top:63px;width:9px;height:9px"><svg><use href="#i-clock"/></svg></div>
  <p class="copy" style="left:27px;top:62px;width:68px">Short note on how our team turns smart data into clear results for every store we serve.</p>
  <div class="dot dot--bright" style="left:13px;top:78px;width:9px;height:9px"><svg><use href="#i-hourglass"/></svg></div>
  <p class="copy" style="left:27px;top:77px;width:68px">Short note on how our team turns smart data into clear results for every store we serve.</p>
  <footer class="foot"><span>We create digital competitiveness</span><span>www.halvoratradeallies.se | 12</span></footer>
</section>

<section class="slide slide--light">
  <div class="ph ph--screen" style="left:0;top:16px;width:99px;height:40px" role="img" aria-label="Photo: woman touching a holographic data screen"></div>
  <div style="left:104px;top:28px;font-size:9px;font-weight:700;line-height:1">HTA</div>
  <div class="title" style="left:137px;top:27px;width:56px;font-weight:300">Our passion is the key factor for customer success</div>
  <div class="ph ph--circuit" style="left:99px;top:56px;width:50px;height:40px" role="img" aria-label="Photo: retail technology icons over a dark background"></div>
  <div class="ph ph--store" style="left:149px;top:56px;width:49px;height:40px" role="img" aria-label="Photo: shoppers in a bright store"></div>
  <div class="dot dot--dark" style="left:13px;top:63px;width:9px;height:9px"><svg><use href="#i-clock"/></svg></div>
  <p class="copy" style="left:27px;top:62px;width:68px">Short note on how our team turns smart data into clear results for every store we serve.</p>
  <div class="dot dot--bright" style="left:13px;top:78px;width:9px;height:9px"><svg><use href="#i-hourglass"/></svg></div>
  <p class="copy" style="left:27px;top:77px;width:68px">Short note on how our team turns smart data into clear results for every store we serve.</p>
  <footer class="foot"><span>We create digital competitiveness</span><span>www.halvoratradeallies.se | 13</span></footer>
</section>

<section class="slide slide--dark">
  <div class="brand">HTA</div>
  <div class="title" style="left:12px;top:20px;width:44px;font-weight:300">We work with the following technologies</div>
  <ul class="list" style="left:15px;top:42px;width:40px">
    <li>Digital Signage</li><li>Sound solutions</li><li>Queue management solutions</li><li>People counter technology</li><li>Visitor Analytics</li><li>Digital real estate solutions</li><li>Media sales digital communication in store</li>
  </ul>
  <div class="ph ph--person-dark" style="left:57px;top:24px;width:48px;height:71px" role="img" aria-label="Photo: person in dark clothing"></div>
  <div class="ph ph--mixer" style="left:105px;top:24px;width:49px;height:71px" role="img" aria-label="Photo: sound mixing desk"></div>
  <div class="ph ph--tablet" style="left:154px;top:24px;width:32px;height:71px" role="img" aria-label="Photo: hand using a tablet"></div>
  <footer class="foot"><span>We create digital competitiveness</span><span>www.halvoratradeallies.se | 17</span></footer>
</section>

<section class="slide slide--light">
  <div class="brand">HTA</div>
  <div class="title" style="left:12px;top:20px;width:44px;font-weight:300">We work with the following technologies</div>
  <ul class="list" style="left:15px;top:42px;width:40px">
    <li>Digital Signage</li><li>Sound solutions</li><li>Queue management solutions</li><li>People counter technology</li><li>Visitor Analytics</li><li>Digital real estate solutions</li><li>Media sales digital communication in store</li>
  </ul>
  <div class="ph ph--person-dark" style="left:57px;top:24px;width:48px;height:71px" role="img" aria-label="Photo: person in dark clothing"></div>
  <div class="ph ph--mixer" style="left:105px;top:24px;width:49px;height:71px" role="img" aria-label="Photo: sound mixing desk"></div>
  <div class="ph ph--tablet" style="left:154px;top:24px;width:32px;height:71px" role="img" aria-label="Photo: hand using a tablet"></div>
  <footer class="foot"><span>We create digital competitiveness</span><span>www.halvoratradeallies.se | 18</span></footer>
</section>

<!-- row 2 -->
<section class="slide slide--dark">
  <div class="brand">HTA</div>
  <div class="title" style="left:12px;top:21px;width:44px;font-weight:300">We work with the following technologies</div>
  <ul class="list" style="left:15px;top:44px;width:40px">
    <li>Digital Signage</li><li>Sound solutions</li><li>Queue management solutions</li><li>People counter technology</li><li>Visitor Analytics</li><li>Digital real estate solutions</li><li>Media sales digital communication in store</li>
  </ul>
  <div class="ph ph--person-dark" style="left:58px;top:24px;width:32px;height:72px" role="img" aria-label="Photo: person in dark clothing"></div>
  <div class="ph ph--globe" style="left:90px;top:24px;width:32px;height:72px" role="img" aria-label="Photo: woman at a digital globe screen"></div>
  <div class="ph ph--mixer" style="left:122px;top:24px;width:32px;height:72px" role="img" aria-label="Photo: sound mixing desk"></div>
  <div class="ph ph--tablet" style="left:154px;top:24px;width:32px;height:72px" role="img" aria-label="Photo: hand using a tablet"></div>
  <footer class="foot"><span>We create digital competitiveness</span><span>www.halvoratradeallies.se | 19</span></footer>
</section>

<section class="slide slide--light">
  <div class="brand">HTA</div>
  <div class="title" style="left:12px;top:21px;width:44px;font-weight:300">We work with the following technologies</div>
  <ul class="list" style="left:15px;top:44px;width:40px">
    <li>Digital Signage</li><li>Sound solutions</li><li>Queue management solutions</li><li>People counter technology</li><li>Visitor Analytics</li><li>Digital real estate solutions</li><li>Media sales digital communication in store</li>
  </ul>
  <div class="ph ph--person-dark" style="left:58px;top:24px;width:32px;height:72px" role="img" aria-label="Photo: person in dark clothing"></div>
  <div class="ph ph--globe" style="left:90px;top:24px;width:32px;height:72px" role="img" aria-label="Photo: woman at a digital globe screen"></div>
  <div class="ph ph--mixer" style="left:122px;top:24px;width:32px;height:72px" role="img" aria-label="Photo: sound mixing desk"></div>
  <div class="ph ph--tablet" style="left:154px;top:24px;width:32px;height:72px" role="img" aria-label="Photo: hand using a tablet"></div>
  <footer class="foot"><span>We create digital competitiveness</span><span>www.halvoratradeallies.se | 20</span></footer>
</section>

<section class="slide slide--dark">
  <div class="brand">HTA</div>
  <div class="ph ph--chart" style="left:0;top:16px;width:100px;height:79px" role="img" aria-label="Photo: printed bar charts and a coffee cup on a desk"></div>
  <div class="dot dot--gray" style="left:107px;top:22px;width:8px;height:8px"><svg><use href="#i-clock"/></svg></div>
  <p class="copy" style="left:123px;top:21px;width:65px">Short note on the service, the tools we use and the value it brings to your stores.</p>
  <div class="dot dot--gray" style="left:107px;top:42px;width:8px;height:8px"><svg><use href="#i-people"/></svg></div>
  <p class="copy" style="left:123px;top:41px;width:65px">Short note on the service, the tools we use and the value it brings to your stores.</p>
  <div class="dot dot--gray" style="left:107px;top:62px;width:8px;height:8px"><svg><use href="#i-hourglass"/></svg></div>
  <p class="copy" style="left:123px;top:61px;width:65px">Short note on the service, the tools we use and the value it brings to your stores.</p>
  <div class="dot dot--bright" style="left:107px;top:82px;width:8px;height:8px"><svg><use href="#i-calendar"/></svg></div>
  <p class="copy" style="left:123px;top:81px;width:65px">Short note on the service, the tools we use and the value it brings to your stores.</p>
  <footer class="foot"><span>We create digital competitiveness</span><span>www.halvoratradeallies.se | 21</span></footer>
</section>

<section class="slide slide--light">
  <div class="brand">HTA</div>
  <div class="ph ph--chart" style="left:0;top:16px;width:100px;height:79px" role="img" aria-label="Photo: printed bar charts and a coffee cup on a desk"></div>
  <div class="dot dot--gray" style="left:107px;top:22px;width:8px;height:8px"><svg><use href="#i-clock"/></svg></div>
  <p class="copy" style="left:123px;top:21px;width:65px">Short note on the service, the tools we use and the value it brings to your stores.</p>
  <div class="dot dot--navy" style="left:107px;top:42px;width:8px;height:8px"><svg><use href="#i-people"/></svg></div>
  <p class="copy" style="left:123px;top:41px;width:65px">Short note on the service, the tools we use and the value it brings to your stores.</p>
  <div class="dot dot--gray" style="left:107px;top:62px;width:8px;height:8px"><svg><use href="#i-hourglass"/></svg></div>
  <p class="copy" style="left:123px;top:61px;width:65px">Short note on the service, the tools we use and the value it brings to your stores.</p>
  <div class="dot dot--bright" style="left:107px;top:82px;width:8px;height:8px"><svg><use href="#i-calendar"/></svg></div>
  <p class="copy" style="left:123px;top:81px;width:65px">Short note on the service, the tools we use and the value it brings to your stores.</p>
  <footer class="foot"><span>We create digital competitiveness</span><span>www.halvoratradeallies.se | 22</span></footer>
</section>

<!-- row 3 -->
<section class="slide slide--dark">
  <div class="brand">HTA</div>
  <div class="title title--center" style="top:8px;font-weight:700">Halvora Trade Allies Core Services</div>
  <div class="sub" style="left:0;right:0;top:15px;text-align:center">Quickly repurpose top-line innovation before global communities</div>
  <div class="band band--accent" style="top:22px;height:39px"></div>
  <div class="band band--gray" style="top:61px;height:37px"></div>
  <div style="left:12px;top:25px;width:56px"><svg class="glyph"><use href="#i-pie"/></svg><div class="label">Your description text</div><p class="copy">A brief line about this service and how it helps your team move faster each day.</p></div>
  <div style="left:75px;top:25px;width:56px"><svg class="glyph"><use href="#i-target"/></svg><div class="label">Your description text</div><p class="copy">A brief line about this service and how it helps your team move faster each day.</p></div>
  <div style="left:137px;top:25px;width:56px"><svg class="glyph"><use href="#i-gauge"/></svg><div class="label">Your description text</div><p class="copy">A brief line about this service and how it helps your team move faster each day.</p></div>
  <div style="left:12px;top:65px;width:56px"><svg class="glyph"><use href="#i-people"/></svg><div class="label">Your description text</div><p class="copy">A brief line about this service and how it helps your team move faster each day.</p></div>
  <div style="left:75px;top:65px;width:56px"><svg class="glyph"><use href="#i-globe"/></svg><div class="label">Your description text</div><p class="copy">A brief line about this service and how it helps your team move faster each day.</p></div>
  <div style="left:137px;top:65px;width:56px"><svg class="glyph"><use href="#i-hourglass"/></svg><div class="label">Your description text</div><p class="copy">A brief line about this service and how it helps your team move faster each day.</p></div>
  <footer class="foot"><span>We create digital competitiveness</span><span>www.halvoratradeallies.se | 23</span></footer>
</section>

<section class="slide slide--light">
  <div class="brand">HTA</div>
  <div class="title title--center" style="top:8px;font-weight:700">Halvora Trade Allies Core Services</div>
  <div class="sub" style="left:0;right:0;top:15px;text-align:center">Quickly repurpose top-line innovation before global communities</div>
  <div class="band band--accent" style="top:22px;height:39px"></div>
  <div class="band band--gray" style="top:61px;height:37px"></div>
  <div style="left:12px;top:25px;width:56px;--ink:#fff;--soft:rgba(255,255,255,.75)"><svg class="glyph"><use href="#i-pie"/></svg><div class="label">Your description text</div><p class="copy">A brief line about this service and how it helps your team move faster each day.</p></div>
  <div style="left:75px;top:25px;width:56px;--ink:#fff;--soft:rgba(255,255,255,.75)"><svg class="glyph"><use href="#i-target"/></svg><div class="label">Your description text</div><p class="copy">A brief line about this service and how it helps your team move faster each day.</p></div>
  <div style="left:137px;top:25px;width:56px;--ink:#fff;--soft:rgba(255,255,255,.75)"><svg class="glyph"><use href="#i-gauge"/></svg><div class="label">Your description text</div><p class="copy">A brief line about this service and how it helps your team move faster each day.</p></div>
  <div style="left:12px;top:65px;width:56px;--ink:#fff;--soft:rgba(255,255,255,.75)"><svg class="glyph"><use href="#i-people"/></svg><div class="label">Your description text</div><p class="copy">A brief line about this service and how it helps your team move faster each day.</p></div>
  <div style="left:75px;top:65px;width:56px;--ink:#fff;--soft:rgba(255,255,255,.75)"><svg class="glyph"><use href="#i-globe"/></svg><div class="label">Your description text</div><p class="copy">A brief line about this service and how it helps your team move faster each day.</p></div>
  <div style="left:137px;top:65px;width:56px;--ink:#fff;--soft:rgba(255,255,255,.75)"><svg class="glyph"><use href="#i-hourglass"/></svg><div class="label">Your description text</div><p class="copy">A brief line about this service and how it helps your team move faster each day.</p></div>
  <footer class="foot"><span>We create digital competitiveness</span><span>www.halvoratradeallies.se | 24</span></footer>
</section>

<section class="slide slide--dark">
  <div class="ph ph--network" style="left:0;top:0;width:198px;height:37px" role="img" aria-label="Photo: connected retail icons over a blurred store"></div>
  <div class="brand" style="color:rgba(255,255,255,.85)">HTA</div>
  <div class="title title--center" style="top:42px;font-weight:500">You could place here the title slide</div>
  <div style="left:12px;top:50px;width:56px"><span class="num">01.</span><span class="label">Your description text</span><p class="copy">Brief note on this step and the value it brings to your business.</p></div>
  <div style="left:76px;top:50px;width:56px"><span class="num">03.</span><span class="label">Your description text</span><p class="copy">Brief note on this step and the value it brings to your business.</p></div>
  <div style="left:139px;top:50px;width:56px"><span class="num">05.</span><span class="label">Your description text</span><p class="copy">Brief note on this step and the value it brings to your business.</p></div>
  <div style="left:12px;top:77px;width:56px"><span class="num">02.</span><span class="label">Your description text</span><p class="copy">Brief note on this step and the value it brings to your business.</p></div>
  <div style="left:76px;top:77px;width:56px"><span class="num">04.</span><span class="label">Your description text</span><p class="copy">Brief note on this step and the value it brings to your business.</p></div>
  <div style="left:139px;top:77px;width:56px"><span class="num">06.</span><span class="label">Your description text</span><p class="copy">Brief note on this step and the value it brings to your business.</p></div>
  <footer class="foot"><span>We create digital competitiveness</span><span>www.halvoratradeallies.se | 25</span></footer>
</section>

<section class="slide slide--light">
  <div class="ph ph--network" style="left:0;top:0;width:198px;height:37px" role="img" aria-label="Photo: connected retail icons over a blurred store"></div>
  <div class="brand" style="color:rgba(255,255,255,.85)">HTA</div>
  <div class="title title--center" style="top:42px;font-weight:500">You could place here the title slide</div>
  <div style="left:12px;top:50px;width:56px"><span class="num">01.</span><span class="label">Your description text</span><p class="copy">Brief note on this step and the value it brings to your business.</p></div>
  <div style="left:76px;top:50px;width:56px"><span class="num">03.</span><span class="label">Your description text</span><p class="copy">Brief note on this step and the value it brings to your business.</p></div>
  <div style="left:139px;top:50px;width:56px"><span class="num">05.</span><span class="label">Your description text</span><p class="copy">Brief note on this step and the value it brings to your business.</p></div>
  <div style="left:12px;top:77px;width:56px"><span class="num">02.</span><span class="label">Your description text</span><p class="copy">Brief note on this step and the value it brings to your business.</p></div>
  <div style="left:76px;top:77px;width:56px"><span class="num">04.</span><span class="label">Your description text</span><p class="copy">Brief note on this step and the value it brings to your business.</p></div>
  <div style="left:139px;top:77px;width:56px"><span class="num">06.</span><span class="label">Your description text</span><p class="copy">Brief note on this step and the value it brings to your business.</p></div>
  <div class="band" style="bottom:0;height:7px;background:var(--navy)"></div>
  <footer class="foot" style="color:rgba(255,255,255,.8);bottom:2.5px"><span>We create digital competitiveness</span><span>www.halvoratradeallies.se | 26</span></footer>
</section>

<!-- row 4 -->
<section class="slide slide--dark">
  <div class="brand">HTA</div>
  <div class="title title--center" style="top:8px;font-weight:700">Halvora Trade Allies Core Services</div>
  <div class="sub" style="left:0;right:0;top:15px;text-align:center">Quickly repurpose top-line innovation before global communities</div>
  <div class="dot dot--white" style="left:18px;top:27px;width:10px;height:10px"><svg><use href="#i-clock"/></svg></div>
  <div style="left:33px;top:27px;width:60px"><div class="label">Your description text</div><p class="copy">Short line about this service and its value.</p></div>
  <div class="dot dot--gray" style="left:18px;top:53px;width:10px;height:10px"><svg><use href="#i-people"/></svg></div>
  <div style="left:33px;top:53px;width:60px"><div class="label">Your description text</div><p class="copy">Short line about this service and its value.</p></div>
  <div class="dot dot--bright" style="left:18px;top:79px;width:10px;height:10px"><svg><use href="#i-hourglass"/></svg></div>
  <div style="left:33px;top:79px;width:60px"><div class="label">Your description text</div><p class="copy">Short line about this service and its value.</p></div>
  <div class="dot dot--bright" style="left:110px;top:27px;width:10px;height:10px"><svg><use href="#i-monitor"/></svg></div>
  <div style="left:125px;top:27px;width:60px"><div class="label">Your description text</div><p class="copy">Short line about this service and its value.</p></div>
  <div class="dot dot--gray" style="left:110px;top:53px;width:10px;height:10px"><svg><use href="#i-target"/></svg></div>
  <div style="left:125px;top:53px;width:60px"><div class="label">Your description text</div><p class="copy">Short line about this service and its value.</p></div>
  <div class="dot dot--gray" style="left:110px;top:79px;width:10px;height:10px"><svg><use href="#i-gauge"/></svg></div>
  <div style="left:125px;top:79px;width:60px"><div class="label">Your description text</div><p class="copy">Short line about this service and its value.</p></div>
  <footer class="foot"><span>We create digital competitiveness</span><span>www.halvoratradeallies.se | 27</span></footer>
</section>

<section class="slide slide--light">
  <div class="brand">HTA</div>
  <div class="title title--center" style="top:8px;font-weight:700">Halvora Trade Allies Core Services</div>
  <div class="sub" style="left:0;right:0;top:15px;text-align:center">Quickly repurpose top-line innovation before global communities</div>
  <div class="dot dot--navy" style="left:18px;top:27px;width:10px;height:10px"><svg><use href="#i-clock"/></svg></div>
  <div style="left:33px;top:27px;width:60px"><div class="label">Your description text</div><p class="copy">Short line about this service and its value.</p></div>
  <div class="dot dot--gray" style="left:18px;top:53px;width:10px;height:10px"><svg><use href="#i-people"/></svg></div>
  <div style="left:33px;top:53px;width:60px"><div class="label">Your description text</div><p class="copy">Short line about this service and its value.</p></div>
  <div class="dot dot--bright" style="left:18px;top:79px;width:10px;height:10px"><svg><use href="#i-hourglass"/></svg></div>
  <div style="left:33px;top:79px;width:60px"><div class="label">Your description text</div><p class="copy">Short line about this service and its value.</p></div>
  <div class="dot dot--bright" style="left:110px;top:27px;width:10px;height:10px"><svg><use href="#i-monitor"/></svg></div>
  <div style="left:125px;top:27px;width:60px"><div class="label">Your description text</div><p class="copy">Short line about this service and its value.</p></div>
  <div class="dot dot--navy" style="left:110px;top:53px;width:10px;height:10px"><svg><use href="#i-target"/></svg></div>
  <div style="left:125px;top:53px;width:60px"><div class="label">Your description text</div><p class="copy">Short line about this service and its value.</p></div>
  <div class="dot dot--gray" style="left:110px;top:79px;width:10px;height:10px"><svg><use href="#i-gauge"/></svg></div>
  <div style="left:125px;top:79px;width:60px"><div class="label">Your description text</div><p class="copy">Short line about this service and its value.</p></div>
  <footer class="foot"><span>We create digital competitiveness</span><span>www.halvoratradeallies.se | 28</span></footer>
</section>

<section class="slide slide--dark">
  <div class="title title--center" style="top:8px;font-weight:700">Our Core Services</div>
  <div class="sub" style="left:0;right:0;top:14px;text-align:center">Quickly repurpose top-line innovation before global communities</div>
  <div class="tile tile--gray" style="left:11px;top:21px;width:40px;height:35px"><svg><use href="#i-image"/></svg><div class="label">Your description text</div><p class="copy">Short note on this service and its value.</p></div>
  <div class="tile tile--mid" style="left:56px;top:21px;width:39px;height:35px"><svg><use href="#i-bank"/></svg><div class="label">Your description text</div><p class="copy">Short note on this service and its value.</p></div>
  <div class="tile tile--slate" style="left:101px;top:21px;width:40px;height:35px"><svg><use href="#i-search"/></svg><div class="label">Your description text</div><p class="copy">Short note on this service and its value.</p></div>
  <div class="tile tile--bright" style="left:146px;top:21px;width:40px;height:35px"><svg><use href="#i-send"/></svg><div class="label">Your description text</div><p class="copy">Short note on this service and its value.</p></div>
  <div class="tile tile--bright" style="left:11px;top:61px;width:40px;height:35px"><svg><use href="#i-calendar"/></svg><div class="label">Your description text</div><p class="copy">Short note on this service and its value.</p></div>
  <div class="tile tile--slate" style="left:56px;top:61px;width:39px;height:35px"><svg><use href="#i-monitor"/></svg><div class="label">Your description text</div><p class="copy">Short note on this service and its value.</p></div>
  <div class="tile tile--slate" style="left:101px;top:61px;width:40px;height:35px"><svg><use href="#i-globe"/></svg><div class="label">Your description text</div><p class="copy">Short note on this service and its value.</p></div>
  <div class="tile tile--gray" style="left:146px;top:61px;width:40px;height:35px"><svg><use href="#i-image"/></svg><div class="label">Your description text</div><p class="copy">Short note on this service and its value.</p></div>
  <footer class="foot"><span>We create digital competitiveness</span><span>www.halvoratradeallies.se | 29</span></footer>
</section>

<section class="slide slide--light">
  <div class="brand">HTA</div>
  <div class="title title--center" style="top:8px;font-weight:700">Our Core Services</div>
  <div class="sub" style="left:0;right:0;top:14px;text-align:center">A short line about the services we offer to you.</div>
  <div class="tile tile--gray" style="left:11px;top:21px;width:40px;height:35px"><svg><use href="#i-image"/></svg><div class="label">Your description text</div><p class="copy">Short note on this service and its value.</p></div>
  <div class="tile tile--slate" style="left:56px;top:21px;width:39px;height:35px"><svg><use href="#i-bank"/></svg><div class="label">Your description text</div><p class="copy">Short note on this service and its value.</p></div>
  <div class="tile tile--slate" style="left:101px;top:21px;width:40px;height:35px"><svg><use href="#i-search"/></svg><div class="label">Your description text</div><p class="copy">Short note on this service and its value.</p></div>
  <div class="tile tile--bright" style="left:146px;top:21px;width:40px;height:35px"><svg><use href="#i-send"/></svg><div class="label">Your description text</div><p class="copy">Short note on this service and its value.</p></div>
  <div class="tile tile--bright" style="left:11px;top:61px;width:40px;height:35px"><svg><use href="#i-calendar"/></svg><div class="label">Your description text</div><p class="copy">Short note on this service and its value.</p></div>
  <div class="tile tile--slate" style="left:56px;top:61px;width:39px;height:35px"><svg><use href="#i-monitor"/></svg><div class="label">Your description text</div><p class="copy">Short note on this service and its value.</p></div>
  <div class="tile tile--navy" style="left:101px;top:61px;width:40px;height:35px"><svg><use href="#i-globe"/></svg><div class="label">Your description text</div><p class="copy">Short note on this service and its value.</p></div>
  <div class="tile tile--gray" style="left:146px;top:61px;width:40px;height:35px"><svg><use href="#i-image"/></svg><div class="label">Your description text</div><p class="copy">Short note on this service and its value.</p></div>
  <footer class="foot"><span>We create digital competitiveness</span><span>www.halvoratradeallies.se | 30</span></footer>
</section>

<!-- row 5 -->
<section class="slide slide--dark">
  <div class="ph ph--globe" style="left:0;top:0;width:61px;height:99px" role="img" aria-label="Photo: woman reaching toward a digital globe"></div>
  <div class="brand">HTA</div>
  <div class="title" style="left:74px;top:10px;font-weight:700">Halvora Trade Allies Service</div>
  <div class="dot dot--white" style="left:74px;top:21px;width:10px;height:10px"><svg><use href="#i-pie"/></svg></div>
  <div style="left:89px;top:21px;width:90px"><div class="label">Your description text</div><p class="copy">Short line about this service and its value.</p></div>
  <div class="dot dot--gray" style="left:74px;top:47px;width:10px;height:10px"><svg><use href="#i-people"/></svg></div>
  <div style="left:89px;top:47px;width:90px"><div class="label">Your description text</div><p class="copy">Short line about this service and its value.</p></div>
  <p class="callout" style="left:72px;top:67px;width:114px;height:28px;background:var(--mid)">A longer note about our service, how we work with our clients and the results we deliver together across every store, screen and channel we manage.</p>
  <footer class="foot" style="left:11px"><span>We create digital competitiveness</span><span>www.halvoratradeallies.se | 41</span></footer>
</section>

<section class="slide slide--light">
  <div class="ph ph--globe" style="left:0;top:0;width:61px;height:99px" role="img" aria-label="Photo: woman reaching toward a digital globe"></div>
  <div class="brand">HTA</div>
  <div class="title" style="left:74px;top:10px;font-weight:700">Halvora Trade Allies Service</div>
  <div class="dot dot--navy" style="left:74px;top:21px;width:10px;height:10px"><svg><use href="#i-pie"/></svg></div>
  <div style="left:89px;top:21px;width:90px"><div class="label">Your description text</div><p class="copy">Short line about this service and its value.</p></div>
  <div class="dot dot--gray" style="left:74px;top:47px;width:10px;height:10px"><svg><use href="#i-people"/></svg></div>
  <div style="left:89px;top:47px;width:90px"><div class="label">Your description text</div><p class="copy">Short line about this service and its value.</p></div>
  <p class="callout" style="left:72px;top:67px;width:114px;height:28px;background:var(--navy)">A longer note about our service, how we work with our clients and the results we deliver together across every store, screen and channel we manage.</p>
  <footer class="foot"><span>We create digital competitiveness</span><span>www.halvoratradeallies.se | 42</span></footer>
</section>

<section class="slide slide--dark">
  <div style="left:11px;top:4px;font-size:7px;font-weight:700;line-height:1">HTA</div>
  <div class="ph ph--globe" style="left:137px;top:0;width:61px;height:99px" role="img" aria-label="Photo: woman reaching toward a digital globe"></div>
  <div class="title" style="left:12px;top:20px;font-weight:500">Halvora Trade Allies Core Services</div>
  <div style="left:12px;top:29px;width:56px"><svg class="glyph"><use href="#i-pie"/></svg><div class="label">Your description text</div><p class="copy">A brief line about this service and how it helps your team move faster each day.</p></div>
  <div style="left:75px;top:29px;width:56px"><svg class="glyph"><use href="#i-target"/></svg><div class="label">Your description text</div><p class="copy">A brief line about this service and how it helps your team move faster each day.</p></div>
  <div style="left:12px;top:62px;width:56px"><svg class="glyph"><use href="#i-people"/></svg><div class="label">Your description text</div><p class="copy">A brief line about this service and how it helps your team move faster each day.</p></div>
  <div style="left:75px;top:62px;width:56px"><svg class="glyph"><use href="#i-globe"/></svg><div class="label">Your description text</div><p class="copy">A brief line about this service and how it helps your team move faster each day.</p></div>
  <footer class="foot"><span>We create digital competitiveness</span><span>www.halvoratradeallies.se | 43</span></footer>
</section>

<section class="slide slide--light">
  <div style="left:11px;top:4px;font-size:7px;font-weight:700;line-height:1">HTA</div>
  <div class="ph ph--globe" style="left:137px;top:0;width:61px;height:99px" role="img" aria-label="Photo: woman reaching toward a digital globe"></div>
  <div class="title" style="left:12px;top:20px;font-weight:500">Halvora Trade Allies Core Services</div>
  <div style="left:12px;top:29px;width:56px"><svg class="glyph"><use href="#i-pie"/></svg><div class="label">Your description text</div><p class="copy">A brief line about this service and how it helps your team move faster each day.</p></div>
  <div style="left:75px;top:29px;width:56px"><svg class="glyph"><use href="#i-target"/></svg><div class="label">Your description text</div><p class="copy">A brief line about this service and how it helps your team move faster each day.</p></div>
  <div style="left:12px;top:62px;width:56px"><svg class="glyph"><use href="#i-people"/></svg><div class="label">Your description text</div><p class="copy">A brief line about this service and how it helps your team move faster each day.</p></div>
  <div style="left:75px;top:62px;width:56px"><svg class="glyph"><use href="#i-globe"/></svg><div class="label">Your description text</div><p class="copy">A brief line about this service and how it helps your team move faster each day.</p></div>
  <footer class="foot"><span>We create digital competitiveness</span><span>www.halvoratradeallies.se | 44</span></footer>
</section>

<!-- row 6 -->
<section class="slide slide--dark">
  <div class="brand">HTA</div>
  <div class="title title--center" style="top:7px;font-weight:700">Halvora Trade Allies Price Table</div>
  <div class="sub" style="left:0;right:0;top:14px;text-align:center">A short line about our prices and the plans we offer.</div>
  <div class="price price--white" style="left:12px;top:24px;width:40px;height:71px"><div class="price__amount">15<small>$</small></div><div class="price__plan">Basic Users</div><p class="copy">Short note on what this plan includes for you.</p><div class="price__btn">Read More</div></div>
  <div class="price price--gray" style="left:57px;top:24px;width:39px;height:71px"><div class="price__amount">50<small>$</small></div><div class="price__plan">Premium Users</div><p class="copy">Short note on what this plan includes for you.</p><div class="price__btn">Read More</div></div>
  <div class="price price--mid" style="left:101px;top:24px;width:40px;height:71px"><div class="price__amount">77<small>$</small></div><div class="price__plan">Unique Users</div><p class="copy">Short note on what this plan includes for you.</p><div class="price__btn">Read More</div></div>
  <div class="price price--white" style="left:146px;top:24px;width:41px;height:71px"><div class="price__amount">97<small>$</small></div><div class="price__plan">Exclusive Users</div><p class="copy">Short note on what this plan includes for you.</p><div class="price__btn">Read More</div></div>
  <footer class="foot"><span>We create digital competitiveness</span><span>www.halvoratradeallies.se | 45</span></footer>
</section>

<section class="slide slide--light">
  <div class="brand">HTA</div>
  <div class="title title--center" style="top:7px;font-weight:700">Halvora Trade Allies Price Table</div>
  <div class="sub" style="left:0;right:0;top:14px;text-align:center">A short line about our prices and the plans we offer.</div>
  <div class="price price--bright" style="left:12px;top:24px;width:40px;height:71px"><div class="price__amount">15<small>$</small></div><div class="price__plan">Basic Users</div><p class="copy">Short note on what this plan includes for you.</p><div class="price__btn">Read More</div></div>
  <div class="price price--gray" style="left:57px;top:24px;width:39px;height:71px;color:#fff"><div class="price__amount">50<small>$</small></div><div class="price__plan">Premium Users</div><p class="copy">Short note on what this plan includes for you.</p><div class="price__btn">Read More</div></div>
  <div class="price price--navy" style="left:101px;top:24px;width:40px;height:71px"><div class="price__amount">77<small>$</small></div><div class="price__plan">Unique Users</div><p class="copy">Short note on what this plan includes for you.</p><div class="price__btn">Read More</div></div>
  <div class="price price--dark" style="left:146px;top:24px;width:41px;height:71px"><div class="price__amount">97<small>$</small></div><div class="price__plan">Exclusive Users</div><p class="copy">Short note on what this plan includes for you.</p><div class="price__btn">Read More</div></div>
  <footer class="foot"><span>We create digital competitiveness</span><span>www.halvoratradeallies.se | 46</span></footer>
</section>

<section class="slide slide--dark">
  <div style="left:125px;top:0;width:73px;height:111px;background:var(--gray)"></div>
  <div class="brand">HTA</div>
  <div class="title" style="left:11px;top:14px;width:60px;font-weight:500">Service distribution for our Digital Options</div>
  <ol class="copy" style="left:11px;top:36px;width:84px;list-style:none">
    <li style="margin-bottom:4px">1. Short note on this option, what it covers and how it helps your business grow.</li>
    <li style="margin-bottom:4px">2. Short note on this option, what it covers and how it helps your business grow.</li>
    <li>3. Short note on this option, what it covers and how it helps your business grow.</li>
  </ol>
  <svg style="left:90px;top:20px;width:70px;height:70px" viewBox="0 0 70 70" role="img" aria-label="Donut chart of service distribution">
    <circle cx="35" cy="35" r="28" fill="none" stroke="#a6a6a6" stroke-width="9"/>
    <circle cx="35" cy="35" r="28" fill="none" stroke="var(--bright)" stroke-width="9" stroke-dasharray="88 88" transform="rotate(-90 35 35)"/>
    <circle cx="35" cy="35" r="28" fill="none" stroke="#3d4550" stroke-width="9" stroke-dasharray="0 132 22 22" transform="rotate(-90 35 35)"/>
    <circle cx="35" cy="35" r="18" fill="none" stroke="#6d7f99" stroke-width="7"/>
    <circle cx="35" cy="35" r="18" fill="none" stroke="var(--mid)" stroke-width="7" stroke-dasharray="60 53" transform="rotate(-90 35 35)"/>
    <circle cx="35" cy="35" r="11" fill="var(--navy)"/>
  </svg>
  <div class="legend" style="left:167px;top:40px">
    <div><i style="background:var(--bright)"></i>Option one</div>
    <div><i style="background:var(--mid)"></i>Option two</div>
    <div><i style="background:#c7c7c7"></i>Option three</div>
    <div><i style="background:#3d4550"></i>Option four</div>
  </div>
  <footer class="foot"><span>We create digital competitiveness</span><span style="color:rgba(255,255,255,.85)">www.halvoratradeallies.se | 47</span></footer>
</section>

<section class="slide slide--light">
  <div style="left:125px;top:0;width:73px;height:111px;background:var(--gray-light)"></div>
  <div class="brand">HTA</div>
  <div class="title" style="left:11px;top:14px;width:60px;font-weight:500">Service distribution for our Digital Options</div>
  <ol class="copy" style="left:11px;top:36px;width:84px;list-style:none">
    <li style="margin-bottom:4px">1. Short note on this option, what it covers and how it helps your business grow.</li>
    <li style="margin-bottom:4px">2. Short note on this option, what it covers and how it helps your business grow.</li>
    <li>3. Short note on this option, what it covers and how it helps your business grow.</li>
  </ol>
  <svg style="left:90px;top:20px;width:70px;height:70px" viewBox="0 0 70 70" role="img" aria-label="Donut chart of service distribution">
    <circle cx="35" cy="35" r="28" fill="none" stroke="#c9ced6" stroke-width="9"/>
    <circle cx="35" cy="35" r="28" fill="none" stroke="var(--bright)" stroke-width="9" stroke-dasharray="88 88" transform="rotate(-90 35 35)"/>
    <circle cx="35" cy="35" r="28" fill="none" stroke="var(--navy)" stroke-width="9" stroke-dasharray="0 88 44 44" transform="rotate(-90 35 35)"/>
    <circle cx="35" cy="35" r="28" fill="none" stroke="#3d4550" stroke-width="9" stroke-dasharray="0 150 26 0" transform="rotate(-90 35 35)"/>
    <circle cx="35" cy="35" r="18" fill="none" stroke="#fff" stroke-width="7"/>
    <circle cx="35" cy="35" r="11" fill="var(--mid)"/>
  </svg>
  <div class="legend" style="left:167px;top:40px">
    <div><i style="background:var(--bright)"></i>Option one</div>
    <div><i style="background:var(--navy)"></i>Option two</div>
    <div><i style="background:#e3e3e3"></i>Option three</div>
    <div><i style="background:#3d4550"></i>Option four</div>
  </div>
  <footer class="foot"><span>We create digital competitiveness</span><span style="color:#fff">www.halvoratradeallies.se | 48</span></footer>
</section>

<!-- row 7 -->
<section class="slide slide--dark">
  <div class="brand">HTA</div>
  <div class="title" style="left:12px;top:9px;font-weight:700">Customer Profile</div>
  <div class="title" style="left:12px;top:15px;font-size:4px;font-weight:300">Service distribution for our Digital Options</div>
  <div style="left:12px;top:24px;width:174px;height:71px;background:#1c5dac"></div>
  <div class="client" style="left:19px;top:28px">Norvik</div>
  <p class="copy" style="left:16px;top:40px;width:32px">Short profile of this customer and the work we have done together.</p>
  <div class="dot dot--navy" style="left:55px;top:30px;width:7px;height:7px"><svg><use href="#i-target"/></svg></div>
  <div style="left:65px;top:30px;width:52px"><div class="caps">CONSULTING PLAN</div><p class="copy">Short note on this plan.</p></div>
  <div class="dot dot--gray" style="left:55px;top:46px;width:7px;height:7px"><svg><use href="#i-target"/></svg></div>
  <div style="left:65px;top:46px;width:52px"><div class="caps">CONSULTING PLAN</div><p class="copy">Short note on this plan.</p></div>
  <p class="copy" style="left:55px;top:68px;width:62px">A short note on the results we delivered for this customer.</p>
  <div class="ph ph--hand" style="left:122px;top:24px;width:32px;height:71px" role="img" aria-label="Photo: hand holding glowing app icons"></div>
  <div class="ph ph--globe" style="left:154px;top:24px;width:32px;height:71px" role="img" aria-label="Photo: woman at a digital globe screen"></div>
  <footer class="foot"><span>We create digital competitiveness</span><span>www.halvoratradeallies.se | 49</span></footer>
</section>

<section class="slide slide--light">
  <div class="brand">HTA</div>
  <div class="title" style="left:12px;top:9px;font-weight:700">Customer Profile</div>
  <div class="title" style="left:12px;top:15px;font-size:4px;font-weight:300">Service distribution for our Digital Options</div>
  <div style="left:12px;top:24px;width:174px;height:71px;background:var(--panel)"></div>
  <div class="client" style="left:19px;top:28px;color:var(--charcoal)">Norvik</div>
  <p class="copy" style="left:16px;top:40px;width:32px">Short profile of this customer and the work we have done together.</p>
  <div class="dot dot--navy" style="left:55px;top:30px;width:7px;height:7px"><svg><use href="#i-target"/></svg></div>
  <div style="left:65px;top:30px;width:52px"><div class="caps">CONSULTING PLAN</div><p class="copy">Short note on this plan.</p></div>
  <div class="dot dot--dark" style="left:55px;top:46px;width:7px;height:7px"><svg><use href="#i-target"/></svg></div>
  <div style="left:65px;top:46px;width:52px"><div class="caps">CONSULTING PLAN</div><p class="copy">Short note on this plan.</p></div>
  <p class="copy" style="left:55px;top:68px;width:62px">A short note on the results we delivered for this customer.</p>
  <div class="ph ph--mixer" style="left:122px;top:24px;width:32px;height:71px" role="img" aria-label="Photo: sound mixing desk"></div>
  <div class="ph ph--person-dark" style="left:154px;top:24px;width:32px;height:71px" role="img" aria-label="Photo: person in dark clothing"></div>
  <footer class="foot"><span>We create digital competitiveness</span><span>www.halvoratradeallies.se | 50</span></footer>
</section>

<section class="slide slide--dark">
  <div class="ph ph--chart" style="left:0;top:0;width:75px;height:111px" role="img" aria-label="Photo: printed bar charts on a desk"></div>
  <div style="left:75px;top:0;width:47px;height:111px;background:var(--charcoal)"></div>
  <div class="client" style="left:80px;top:18px;color:#fff">Norvik</div>
  <p class="copy" style="left:79px;top:30px;width:39px;color:rgba(255,255,255,.75)">A short profile of this customer, the work we did together and the results we reached.</p>
  <div class="brand">HTA</div>
  <div class="dot dot--bright" style="left:128px;top:24px;width:11px;height:11px"><svg><use href="#i-monitor"/></svg></div>
  <div style="left:143px;top:24px;width:48px"><div class="label">Your description text</div><p class="copy">Short note on this service and its value.</p></div>
  <div class="dot dot--navy" style="left:128px;top:50px;width:11px;height:11px;border:.6px solid #fff"><svg><use href="#i-target"/></svg></div>
  <div style="left:143px;top:50px;width:48px"><div class="label">Your description text</div><p class="copy">Short note on this service and its value.</p></div>
  <div class="dot dot--gray" style="left:128px;top:76px;width:11px;height:11px"><svg><use href="#i-gauge"/></svg></div>
  <div style="left:143px;top:76px;width:48px"><div class="label">Your description text</div><p class="copy">Short note on this service and its value.</p></div>
  <footer class="foot" style="left:128px"><span></span><span>www.halvoratradeallies.se | 51</span></footer>
</section>

<section class="slide slide--light">
  <div class="ph ph--chart" style="left:0;top:0;width:75px;height:111px" role="img" aria-label="Photo: printed bar charts on a desk"></div>
  <div style="left:75px;top:0;width:47px;height:111px;background:var(--charcoal)"></div>
  <div class="client" style="left:80px;top:18px;color:#fff">Norvik</div>
  <p class="copy" style="left:79px;top:30px;width:39px;color:rgba(255,255,255,.75)">A short profile of this customer, the work we did together and the results we reached.</p>
  <div class="brand">HTA</div>
  <div class="dot dot--bright" style="left:128px;top:24px;width:11px;height:11px"><svg><use href="#i-monitor"/></svg></div>
  <div style="left:143px;top:24px;width:48px"><div class="label">Your description text</div><p class="copy">Short note on this service and its value.</p></div>
  <div class="dot dot--navy" style="left:128px;top:50px;width:11px;height:11px;border:.6px solid #fff"><svg><use href="#i-target"/></svg></div>
  <div style="left:143px;top:50px;width:48px"><div class="label">Your description text</div><p class="copy">Short note on this service and its value.</p></div>
  <div class="dot dot--gray" style="left:128px;top:76px;width:11px;height:11px"><svg><use href="#i-gauge"/></svg></div>
  <div style="left:143px;top:76px;width:48px"><div class="label">Your description text</div><p class="copy">Short note on this service and its value.</p></div>
  <footer class="foot" style="left:128px"><span></span><span>www.halvoratradeallies.se | 52</span></footer>
</section>

</main>
</body>
</html>
```